Kelvane Plumbing Business cards

Company is Kelvane Plumbing.
name Dashel Morrowby, I am a plumber, drainer, gasfitter and roofer
Mobile: 0431 906 154
Email address: info@kelvaneplumbing.example (check out my website for some ideas)
Website: www.kelvaneplumbing.example
ABN: 82 916 203 471
LIC: 604517K

I am reliable all round plumber. I am a 24 hour emergency service. Kelvane Plumbing is a professional plumbing service in the Illawarra, South Coast, Southern Sydney and Southern Highland regions of NSW. We offer a 24 hour emergency service for piece of mind to our customers. Call us now to see how we can help you. Kelvane Plumbing approaches every job with attention to detail and excellent customer service. With our superior workmanship you can be confident that the job will be done right the first time around. You can rest assured with results that are guaranteed to last.

Target Market(s)

the general public

Contact Information for Business Card

look up website for some ideas something with similar colours to logo and new modern and to catch the eye.

Colors
fdfdfd
ffffff
000000
7f7f7f
aaaaaa
33a6d7
0492cd

Requirements
Must have
• all contact details
• company- Kelvane Plumbing
• name- Dashel Morrowby
• number mobile- 0431 906 154
• Email address- info@kelvaneplumbing.example
• Website- www.kelvaneplumbing.example
• ABN- 82 916 203 471
• LIC- 604517K

```html
<!DOCTYPE html>
<html lang="en">
<head>
<meta charset="utf-8">
<title>Kelvane Plumbing – Business Cards</title>
<link rel="stylesheet" href="https://fonts.googleapis.com/css2?family=Open+Sans:wdth,wght@75..100,400..700&display=swap">
<style>
  :root {
    --backdrop: #2a2827;
    --card: #070707;
    --blue: #1e9ad2;
    --grey: #7f7f7f;
    --white: #fdfdfd;
  }
  * { box-sizing: border-box; margin: 0; padding: 0; }
  html, body {
    width: 1200px; height: 1200px; overflow: hidden;
    background: var(--backdrop);
    font-family: "Open Sans", Arial, sans-serif;
  }
  .sheet {
    position: relative; width: 1200px; height: 1200px;
    display: flex; justify-content: center; align-items: center; gap: 70px;
  }
  .card {
    width: 450px; height: 740px;
    background: var(--card);
    border-radius: 22px;
    box-shadow: 0 18px 40px rgba(0,0,0,.45);
    display: flex; flex-direction: column; align-items: center;
    color: var(--white);
    text-align: center;
  }
  /* front */
  .card--front { justify-content: flex-start; padding-top: 170px; }
  .brand-mark {
    display: flex; flex-direction: column; align-items: center; gap: 22px;
  }
  .brand-mark__dot {
    width: 64px; height: 64px; border-radius: 50%;
    background: var(--blue);
  }
  .brand-mark__name {
    font-size: 34px; font-weight: 600; letter-spacing: 3px;
    color: var(--blue); text-transform: uppercase; line-height: 1.25;
  }
  .services {
    list-style: none; margin-top: 150px;
    font-stretch: 82%; font-weight: 600; font-size: 27px; line-height: 1.42;
    text-transform: uppercase;
  }
  /* back */
  .card--back { padding-top: 120px; }
  .card--back .brand-mark__name { font-size: 32px; }
  .holder {
    margin-top: 58px;
    font-stretch: 80%; font-weight: 600; font-size: 34px;
    color: var(--blue); text-transform: uppercase; letter-spacing: .5px;
  }
  .contacts { list-style: none; margin-top: 38px; display: flex; flex-direction: column; gap: 20px; }
  .contact { display: flex; flex-direction: column; align-items: center; gap: 8px; font-size: 20px; }
  .contact__icon { width: 30px; height: 30px; }
  .registry {
    margin-top: 62px; font-size: 19px; line-height: 1.45;
    font-stretch: 90%;
  }
  .registry dt { display: inline; color: var(--blue); font-weight: 600; }
  .registry dd { display: inline; }
</style>
</head>
<body>
<main class="sheet">
  <section class="card card--front" aria-label="Card front">
    <div class="brand-mark">
      <span class="brand-mark__dot"></span>
      <span class="brand-mark__name">Kelvane<br>Plumbing</span>
    </div>
    <ul class="services">
      <li>Plumbing</li>
      <li>Drainage</li>
      <li>Gasfitting</li>
      <li>Roofing</li>
    </ul>
  </section>

  <section class="card card--back" aria-label="Card back">
    <div class="brand-mark">
      <span class="brand-mark__name">Kelvane Plumbing</span>
    </div>
    <h1 class="holder">Dashel Morrowby</h1>
    <ul class="contacts">
      <li class="contact">
        <svg class="contact__icon" viewBox="0 0 30 30" aria-hidden="true">
          <circle cx="15" cy="15" r="15" fill="var(--blue)"/>
          <rect x="10.5" y="6.5" width="9" height="17" rx="1.8" fill="none" stroke="#070707" stroke-width="1.8"/>
          <circle cx="15" cy="20.5" r="1" fill="#070707"/>
        </svg>
        <span>0431 906 154</span>
      </li>
      <li class="contact">
        <svg class="contact__icon" viewBox="0 0 30 30" aria-hidden="true">
          <circle cx="15" cy="15" r="15" fill="var(--blue)"/>
          <rect x="8" y="10" width="14" height="10" fill="none" stroke="#070707" stroke-width="1.6"/>
          <path d="M8 10 L15 16 L22 10" fill="none" stroke="#070707" stroke-width="1.6"/>
        </svg>
        <span>info@kelvaneplumbing.example</span>
      </li>
      <li class="contact">
        <svg class="contact__icon" viewBox="0 0 30 30" aria-hidden="true">
          <circle cx="15" cy="15" r="14" fill="none" stroke="var(--blue)" stroke-width="2"/>
          <ellipse cx="15" cy="15" rx="6" ry="14" fill="none" stroke="var(--blue)" stroke-width="1.5"/>
          <path d="M1 15 H29 M4 8 H26 M4 22 H26" stroke="var(--blue)" stroke-width="1.5"/>
        </svg>
        <span>www.kelvaneplumbing.example</span>
      </li>
    </ul>
    <dl class="registry">
      <div><dt>ABN:</dt> <dd>82 916 203 471</dd></div>
      <div><dt>LIC:</dt> <dd>604517K</dd></div>
    </dl>
  </section>
</main>
</body>
</html>
```